Attention grabbing 6x9 postcard

We are looking to have an attention grabbing post card that be sent out to homeowners from our roofing company Olum Roofing. the concept is that on the front it will say something like (STOP THE KNOCKING!
Tired of roofers knocking on your door? Contact us because we value your time as much as you value the roof over your head."
Olum Roofing
OlumRoofing.com
877.612.OLUM
info@olumroofing.com

Please feel free to come up with something very creative. Once we pick the final design we will provide the copy.

```html
<!DOCTYPE html>
<html lang="en">
<head>
<meta charset="utf-8">
<title>Olum Roofing Postcard</title>
<link href="https://fonts.googleapis.com/css2?family=Archivo+Black&family=Great+Vibes&family=Poppins:wght@400;500;600;700;800&display=swap" rel="stylesheet">
<style>
:root{
  --stage:#7d7d7d;
  --gold:#e4ac27;
  --bright:#ffe600;
  --ink:#231f20;
  --charcoal:#3a3a3a;
  --paper:#ffffff;
  --mist:#e8e8e8;
  --ghost:#dedede;
}
*{margin:0;padding:0;box-sizing:border-box}
html,body{width:896px;height:1200px;overflow:hidden}
body{background:var(--stage);font-family:"Poppins",sans-serif;color:var(--ink);position:relative}
.side-label{position:absolute;left:0;width:896px;text-align:center;color:var(--paper);font-family:"Poppins",sans-serif;font-weight:700;font-size:21px;letter-spacing:11px}
.side-label.front{top:45px}
.side-label.back{top:597px}
.card{position:absolute;left:79px;overflow:hidden;background:var(--paper)}
.card-front{top:82px;width:742px;height:502px}
.card-back{top:634px;width:748px;height:506px}
.card svg.bg{position:absolute;left:0;top:0}
.abs{position:absolute}

/* front */
.brand-name{left:0;width:250px;top:106px;text-align:center;font-weight:500;font-size:17px;letter-spacing:.4px;color:var(--ink);display:flex;align-items:center;justify-content:center;gap:8px}
.brand-name .mark{width:12px;height:12px;background:var(--ink)}
.headline-stop{left:440px;top:20px;font-family:"Archivo Black",sans-serif;font-size:80px;line-height:1;color:var(--ink);letter-spacing:-1px}
.headline-the{left:653px;top:61px;font-family:"Archivo Black",sans-serif;font-size:30px;line-height:1;color:var(--ink)}
.headline-knock{left:390px;top:96px;font-family:"Archivo Black",sans-serif;font-size:53px;line-height:1;color:var(--bright);-webkit-text-stroke:2px var(--ink);letter-spacing:-1px}
.tagline{left:392px;top:142px;font-size:21px;line-height:1;color:var(--ink)}
.tagline-door{left:508px;top:163px;font-weight:800;font-size:33px;line-height:1;color:var(--ink);letter-spacing:-.5px}
.tagline-q{left:694px;top:141px;font-weight:800;font-size:56px;line-height:1;color:var(--ink)}
.contact-title{left:36px;top:338px;font-weight:700;font-size:27px;line-height:1;color:var(--gold)}
.contact-copy{left:40px;top:371px;font-size:14.3px;line-height:16.5px;color:var(--ink)}
.contact-script{left:40px;top:403px;font-family:"Great Vibes",cursive;font-size:20px;color:var(--ink)}
.pill{position:absolute;display:flex;align-items:center;justify-content:center;gap:7px;font-weight:600;clip-path:polygon(12px 0,calc(100% - 12px) 0,100% 50%,calc(100% - 12px) 100%,12px 100%,0 50%)}
.pill svg{flex:none}
.pill.gold{background:var(--gold);color:var(--ink)}
.pill.white{background:var(--paper);color:var(--ink)}
.pill.dark{background:var(--charcoal);color:var(--paper)}
.card-front .pill{height:33px;top:442px;font-size:18px}

/* back */
.services-title{left:27px;top:26px;font-family:"Archivo Black",sans-serif;font-size:22px;line-height:1;color:var(--ink)}
.services-copy{left:27px;top:53px;width:320px;font-size:10.6px;line-height:12.3px;color:var(--ink)}
.process-title{left:100px;width:175px;top:150px;text-align:center;font-weight:700;font-size:23px;line-height:22px;color:var(--charcoal);letter-spacing:-.3px}
.process-title span{display:block;color:var(--gold)}
.step-num{width:60px;text-align:center;font-weight:700;font-size:26px;line-height:1;color:var(--ink)}
.step-copy{width:112px;text-align:center;font-size:9.8px;line-height:11.3px;color:var(--ink)}
.divider{width:1px;background:var(--ink);opacity:.6}
.card-back .pill{height:25px;font-size:14px}
.ghost-name{left:480px;width:230px;top:334px;text-align:center;font-size:20px;letter-spacing:.3px;color:var(--ghost)}
.stamp{left:649px;top:17px;width:81px;height:91px;border:1px solid #bdbdbd}
</style>
</head>
<body>

<div class="side-label front">FRONT</div>

<section class="card card-front" aria-label="Postcard front">
  <svg class="bg" width="742" height="502" viewBox="0 0 742 502">
    <defs>
      <linearGradient id="steel" x1="0" y1="0" x2="1" y2="1">
        <stop offset="0" stop-color="#9a9a9a"/>
        <stop offset=".35" stop-color="#f4f4f4"/>
        <stop offset=".7" stop-color="#8c8c8c"/>
        <stop offset="1" stop-color="#d6d6d6"/>
      </linearGradient>
      <linearGradient id="vanTone" x1="0" y1="0" x2="0" y2="1">
        <stop offset="0" stop-color="#c99a2a"/>
        <stop offset=".35" stop-color="#4a4440"/>
        <stop offset="1" stop-color="#2a2624"/>
      </linearGradient>
      <linearGradient id="roofTone" x1="0" y1="0" x2="0" y2="1">
        <stop offset="0" stop-color="#5d83c4"/>
        <stop offset=".5" stop-color="#b58e62"/>
        <stop offset="1" stop-color="#4a4d55"/>
      </linearGradient>
      <linearGradient id="houseTone" x1="0" y1="0" x2="0" y2="1">
        <stop offset="0" stop-color="#a7b3c4"/>
        <stop offset=".5" stop-color="#8a8a86"/>
        <stop offset="1" stop-color="#6f6e6a"/>
      </linearGradient>
    </defs>
    <polygon points="258,0 742,0 742,502 258,502" fill="#e4ac27"/>
    <polygon points="0,0 258,0 430,260 250,502 0,502" fill="#ffffff"/>
    <polygon points="0,157 30,157 116,321 0,321" fill="#e4ac27"/>
    <polygon points="220,0 252,0 420,238 395,250" fill="url(#steel)"/>
    <polygon points="266,0 292,0 370,108 344,108" fill="#ffe600"/>
    <polygon role="img" aria-label="Photo of a new shingled roof with dormers" points="31,170 182,170 253,290 100,290" fill="url(#roofTone)"/>
    <polygon role="img" aria-label="Photo of a house gable with grey siding" points="182,170 347,170 400,245 310,290 253,290" fill="url(#houseTone)"/>
    <polygon role="img" aria-label="Photo of branded roofing service vans with ladders" points="236,210 742,210 742,447 290,447 300,360" fill="url(#vanTone)"/>
    <polygon points="230,430 742,430 742,502 60,502" fill="#231f20"/>
  </svg>

  <div class="abs brand-name"><span class="mark"></span>OLUMROOFING.COM</div>

  <div class="abs headline-stop">STOP</div>
  <div class="abs headline-the">THE</div>
  <div class="abs headline-knock">KNOCKING!</div>
  <div class="abs tagline">Tired of roofers knocking on</div>
  <div class="abs tagline-door">your door</div>
  <div class="abs tagline-q">?</div>

  <div class="abs contact-title">Contact us</div>
  <div class="abs contact-copy">because we value your time as<br>much as you value the roof</div>
  <div class="abs contact-script">over your head.</div>

  <div class="pill gold" style="left:24px;width:209px">
    <svg width="17" height="17" viewBox="0 0 20 20" fill="none" stroke="#231f20" stroke-width="1.4"><circle cx="10" cy="10" r="8.5"/><ellipse cx="10" cy="10" rx="4" ry="8.5"/><path d="M1.5 10h17M3 5.5h14M3 14.5h14M10 1.5v17"/></svg>
    OlumRoofing.com
  </div>
  <div class="pill white" style="left:244px;width:209px">
    <svg width="15" height="15" viewBox="0 0 24 24" fill="#231f20"><path d="M6.6 10.8a15.1 15.1 0 0 0 6.6 6.6l2.2-2.2a1 1 0 0 1 1-.25 11.4 11.4 0 0 0 3.6.57 1 1 0 0 1 1 1V20a1 1 0 0 1-1 1A17 17 0 0 1 3 4a1 1 0 0 1 1-1h3.5a1 1 0 0 1 1 1c0 1.25.2 2.45.57 3.57a1 1 0 0 1-.25 1z"/></svg>
    877.612.OLUM
  </div>
  <div class="pill gold" style="left:461px;width:257px">
    <svg width="22" height="16" viewBox="0 0 22 16" fill="none" stroke="#231f20" stroke-width="1.4"><rect x=".7" y=".7" width="20.6" height="14.6"/><path d="M.7 .7l10.3 8 10.3-8M.7 15.3l7.5-7M21.3 15.3l-7.5-7"/></svg>
    info@olumroofing.com
  </div>
</section>

<div class="side-label back">BACK</div>

<section class="card card-back" aria-label="Postcard back">
  <svg class="bg" width="748" height="506" viewBox="0 0 748 506">
    <defs>
      <linearGradient id="steelBack" x1="0" y1="0" x2="0" y2="1">
        <stop offset="0" stop-color="#e8e8e8"/>
        <stop offset=".3" stop-color="#8a8a8a"/>
        <stop offset=".5" stop-color="#f2f2f2"/>
        <stop offset=".75" stop-color="#7a7a7a"/>
        <stop offset="1" stop-color="#bdbdbd"/>
      </linearGradient>
      <linearGradient id="workTone" x1="0" y1="0" x2="1" y2="0">
        <stop offset="0" stop-color="#e6e6e6"/>
        <stop offset=".6" stop-color="#d9d9d9"/>
        <stop offset="1" stop-color="#efefef"/>
      </linearGradient>
    </defs>
    <polygon role="img" aria-label="Faded photo of a roofer at work with tools" points="0,139 371,139 447,253 377,394 0,394" fill="url(#workTone)"/>
    <polygon points="0,0 282,0 371,139 0,139" fill="#e4ac27"/>
    <polygon points="282,0 323,0 494,253 326,506 288,506 452,253" fill="url(#steelBack)"/>
    <path d="M68 139 V205 L184 252 L290 205 V139" fill="none" stroke="#3a3a3a" stroke-width="22" stroke-linejoin="miter"/>
    <rect x="60" y="139" width="255" height="0" fill="none"/>
    <polygon points="79,185 108,201 108,235 79,251 50,235 50,201" fill="#fff" stroke="#e4ac27" stroke-width="3"/>
    <polygon points="184,207 213,223 213,257 184,273 155,257 155,223" fill="#fff" stroke="#e4ac27" stroke-width="3"/>
    <polygon points="288,185 317,201 317,235 288,251 259,235 259,201" fill="#fff" stroke="#e4ac27" stroke-width="3"/>
  </svg>

  <div class="abs services-title">SERVICES</div>
  <p class="abs services-copy">Olum Roofing offers an array of roofing solutions while providing professional, honest recommendations that address your specific needs. You can always count on us for exceptional service from the moment we meet. From inspection to installation, OLUM has you covered.</p>

  <div class="abs process-title">OLUM ROOFING<span>PROCESS</span></div>

  <div class="abs step-num" style="left:49px;top:205px">01</div>
  <div class="abs step-num" style="left:154px;top:227px">02</div>
  <div class="abs step-num" style="left:258px;top:205px">03</div>

  <p class="abs step-copy" style="left:22px;top:263px">Complementary consultation to access your roofing needs and review our honest recommendations.</p>
  <p class="abs step-copy" style="left:128px;top:286px;width:80px">Our team of professionals replace, restore, or repair your roof making the process as stress-free as possible.</p>
  <p class="abs step-copy" style="left:233px;top:263px">100% satisfaction, peace of mind, and continued professional coverage backed by OLUM Protection*.</p>

  <div class="abs divider" style="left:134px;top:291px;height:79px"></div>
  <div class="abs divider" style="left:228px;top:291px;height:79px"></div>

  <div class="pill gold" style="left:29px;top:421px;width:160px">
    <svg width="14" height="14" viewBox="0 0 20 20" fill="none" stroke="#231f20" stroke-width="1.4"><circle cx="10" cy="10" r="8.5"/><ellipse cx="10" cy="10" rx="4" ry="8.5"/><path d="M1.5 10h17M3 5.5h14M3 14.5h14M10 1.5v17"/></svg>
    OlumRoofing.com
  </div>
  <div class="pill dark" style="left:193px;top:421px;width:160px">
    <svg width="12" height="12" viewBox="0 0 24 24" fill="#ffffff"><path d="M6.6 10.8a15.1 15.1 0 0 0 6.6 6.6l2.2-2.2a1 1 0 0 1 1-.25 11.4 11.4 0 0 0 3.6.57 1 1 0 0 1 1 1V20a1 1 0 0 1-1 1A17 17 0 0 1 3 4a1 1 0 0 1 1-1h3.5a1 1 0 0 1 1 1c0 1.25.2 2.45.57 3.57a1 1 0 0 1-.25 1z"/></svg>
    877.612.OLUM
  </div>
  <div class="pill gold" style="left:29px;top:453px;width:196px">
    <svg width="18" height="13" viewBox="0 0 22 16" fill="none" stroke="#231f20" stroke-width="1.4"><rect x=".7" y=".7" width="20.6" height="14.6"/><path d="M.7 .7l10.3 8 10.3-8M.7 15.3l7.5-7M21.3 15.3l-7.5-7"/></svg>
    info@olumroofing.com
  </div>

  <div class="abs stamp" aria-label="Postage area"></div>
  <div class="abs ghost-name">OLUMROOFING.COM</div>
</section>

</body>
</html>
```